■サイトマップ
★:Gナビに掲載希望

TOP ★
写真館のこと ★
料金一覧 ★
店舗情報 ★
スタッフ紹介
ギャラリー ★
お子さまの成長の記念に(七五三)
思い出やこだわりにあわせた屋外撮影(ロケーション・出張撮影)
季節限定!キャンペーンフォト
キッズ・ベビー・お宮参りの撮影もおまかせください
成人の節目に晴れ姿を撮影
入園・入学・卒業
そのほかの撮影
よくある質問 ★
お問い合わせ(追従ボタン)
ブログ
ニュース

※お子さまの記念~そのほかの撮影のページ
「撮影のこだわり」という文言をGナビに配置して
プルダウンで表示させたいです。

■ターゲット
30~40代 主婦層にあわせて作る
店舗へ電話をかけてくるのはお母さんのため。

■TOPで目立たせたいコンテンツ
・季節限定!キャンペーンフォト
・思い出やこだわりにあわせた屋外撮影(ロケーション・出張撮影)

■上記以外でTOPに掲載したいコンテンツ
・ギャラリー
・写真館のこと
・七五三
・ブログ(更新頻度は低め)
・ニュース(更新頻度は低め)
・元気いっぱいなお子さまの撮影はお任せください!(リンクなし)
・スタッフ紹介

■デザインについて
・英語表記をする際は日本語表記もそえてください。
・Gナビを英語表記にする際は、オンカーソルで日本語表記が出るようにしてほしいです。
・子供の写真は幼稚園~小学校くらいの年齢をメインにしてください。
・キャンペーンページへの追従ボタンを配置。
・メインスライドは大きく、写真がよく見えるように。
・画像を大きめに載せたいです。

■デザイン参考サイト
http://moribana-kobo.jp/
業種やことなりますが、Gナビがおしゃれです。

https://www.lumelle-atelier.com/
シンプルで遊び心が感じられます。
手書き風のイラストがかわいいです。

https://www.tovimo.com/kids/
撮影メニュー・催事の項目で取り扱いプランの一覧がわかっていいです。

■フォントについて
WEB上で使用可能な無料のフォントで作成お願い致します。
OSに紐づくフォントの使用は控えていただければと思います。
(ヒラギノなど)

===============================
●ロゴ
https://hakobox-share.jp/download/7b1e9d2a6c3f85e0a4d71b6c9f02e58d3a1c7b4e
ダウンロードパスワード 7mwz3rpt

●素材
https://hakobox-share.jp/download/9e5c2b7f1a08d46c3e97b2f0d51a8c6e4b3f7d21
ダウンロードパスワード 7mwz3rpt
http://www.fh-taniyama.com/
1ページ
シンプル 複雑
単色 カラフル
暗い 明るい
日常 高級
遊び心 厳粛
未来的 伝統的
女性的 男性的
茶系、緑系、グレー系
• イラストレーター形式 (.ai)
• フォトショップ形式 (.psd)
• PNG形式 (.png)
◆文言について
現行サイトの文章を使用してOKです。

◆素材について
素材として必要なものがある場合には、Velmora Pics画像をご使用ください。
その際、通常アセットでダウンロード出来る画像のみを使用してください。
Velmora Pics以外の素材を使用する際には、
必ず無料で提供いただける物のみご使用ください。

◆注意
店舗へ直接の問い合わせはおやめください。
すでに案をご提出くださった方々、ご応募いただきありがとうございます。
せっかくですので開催期間を延長したいと思います。
何卒よろしくお願いいたします。

雰囲気がにぎやかすぎず渋すぎず、ちょうどよかったため。

この度は選定について大変お待たせいたしました。
また機会がありましたら何卒よろしくお願いいたします。

```html
<!DOCTYPE html>
<html lang="ja">
<head>
<meta charset="utf-8">
<title>谷山写真館</title>
<link rel="stylesheet" href="https://fonts.googleapis.com/css2?family=Noto+Sans+JP:wght@400;500;700&family=Noto+Serif+JP:wght@400;500;700&display=swap">
<style>
:root{
  --ink:#333333;
  --teal:#2f4d52;
  --accent:#e08a3c;
  --beige:#f6ecdf;
  --nav:#f2f2f2;
  --band:#f3f3f3;
  --card:#d49a5e;
  --line:#dddddd;
  --white:#ffffff;
}
*{margin:0;padding:0;box-sizing:border-box}
html,body{width:1200px;height:3348px;overflow:hidden;background:var(--white)}
body{position:relative;font-family:"Noto Sans JP",sans-serif;color:var(--ink)}
.topbar{position:absolute;left:0;top:0;width:1200px;height:34px;background:var(--beige);font-size:13px;text-align:center;line-height:34px;letter-spacing:.05em}
.brand{position:absolute;left:0;top:64px;width:1200px;display:flex;justify-content:center;align-items:center;gap:14px}
.brand-mark{width:30px;height:30px;border-radius:50%;background:var(--ink)}
.brand-name{font-family:"Noto Serif JP",serif;font-size:40px;font-weight:700;letter-spacing:.08em;color:var(--ink)}
.brand-sub{font-family:"Noto Serif JP",serif;font-size:13px;font-weight:700;color:var(--ink);line-height:1.2;margin-left:6px}
.gnav{position:absolute;left:0;top:168px;width:1200px;height:44px;background:var(--nav);display:flex;justify-content:center;gap:58px;align-items:center;font-size:14px}
.gnav .current{color:var(--accent);font-weight:700}
.hero{position:absolute;left:0;top:222px;width:1200px;height:520px;
  background:
    radial-gradient(ellipse 260px 200px at 62% 28%,rgba(92,58,38,.85),rgba(92,58,38,0) 70%),
    radial-gradient(ellipse 220px 170px at 82% 55%,rgba(246,220,200,.95),rgba(246,220,200,0) 75%),
    radial-gradient(ellipse 320px 140px at 58% 92%,rgba(96,132,176,.75),rgba(96,132,176,0) 75%),
    radial-gradient(ellipse 200px 160px at 68% 58%,rgba(238,196,170,.9),rgba(238,196,170,0) 75%),
    linear-gradient(90deg,#ffffff 0%,#fbf8f4 35%,#f3ebe2 60%,#f7f2ec 100%)}
.hero-copy{position:absolute;left:96px;top:365px;font-family:"Noto Serif JP",serif;font-size:38px;line-height:1.45;color:var(--teal);letter-spacing:.06em}
.about-photo{position:absolute;left:58px;top:872px;width:424px;height:550px;background:linear-gradient(160deg,#d9c7ae,#9a8a72 55%,#5f6b4f)}
.about-label{position:absolute;left:72px;top:888px;writing-mode:vertical-rl;font-family:"Noto Serif JP",serif;font-size:26px;background:rgba(255,255,255,.85);padding:14px 8px;letter-spacing:.1em}
.about-body{position:absolute;left:540px;top:895px;width:600px}
.about-body h2{font-family:"Noto Serif JP",serif;font-size:22px;font-weight:700;line-height:1.5}
.about-body p{font-size:14px;line-height:2;margin-top:28px}
.kids-text{position:absolute;left:60px;top:1585px;width:460px;font-size:14px;line-height:2}
.kids-text p+p{margin-top:20px}
.kids-photo{position:absolute;left:700px;top:1460px;width:420px;height:540px;background:linear-gradient(180deg,#fbf6f0,#f1e2d0 60%,#e7d2bb)}
.kids-title{position:absolute;left:720px;top:1480px;writing-mode:vertical-rl;font-family:"Noto Serif JP",serif;font-size:28px;line-height:1.7;letter-spacing:.08em;color:var(--ink)}
.kids-title .hl{color:var(--accent)}
.news{position:absolute;left:0;top:2140px;width:1200px;height:300px;background:var(--band)}
.news-col{position:absolute;top:80px;width:440px}
.news-col h3{font-size:18px;font-weight:700;margin-bottom:22px;border-bottom:1px solid var(--line);padding-bottom:8px}
.news-col li{list-style:none;font-size:14px;line-height:2.4}
.corner{position:absolute;top:0}
.staff-title{position:absolute;left:0;top:2565px;width:1200px;text-align:center;font-size:26px;font-weight:700;letter-spacing:.1em}
.staff-card{position:absolute;top:2728px;width:344px;height:612px}
.staff-card .bg{position:absolute;left:0;top:150px;width:344px;height:462px;background:var(--card)}
.staff-card .photo{position:absolute;left:18px;top:0;width:308px;height:290px}
.staff-card .role{position:absolute;left:26px;top:312px;font-size:14px;color:var(--white)}
.staff-card .name{position:absolute;left:26px;top:338px;font-family:"Noto Serif JP",serif;font-size:32px;font-weight:700;color:var(--white);letter-spacing:.15em;line-height:1.3}
.staff-card .bio{position:absolute;left:26px;top:400px;width:296px;font-size:14px;line-height:1.9;color:var(--white)}
</style>
</head>
<body>
<div class="topbar">採用通信お問い合わせはこちら　0120-48-2715</div>

<header class="brand">
  <span class="brand-mark"></span>
  <span class="brand-name">谷山写真館</span>
  <span class="brand-sub">photostudio<br>taniyama</span>
</header>

<nav class="gnav">
  <span class="current">HOME</span><span>写真館のこと</span><span>料金一覧</span><span>撮影のこだわり ▾</span><span>店舗情報</span><span>ギャラリー</span><span>よくある質問</span><span>お問い合わせ</span>
</nav>

<section class="hero" role="img" aria-label="寝転ぶ赤ちゃんに頬を寄せる女の子の写真"></section>
<p class="hero-copy">特別な毎日を<br>残る形に。</p>

<div class="about-photo" role="img" aria-label="写真館の店舗外観と入口の植物"></div>
<div class="about-label">写真館のこと</div>
<div class="about-body">
  <h2>谷山写真館<br>記念写真・スタジオ撮影・出張撮影・証明写真</h2>
  <p>緑ヶ丘駅前　谷山写真館では</p>
  <p>その他に、お宮参り、百日祝い(お食い初め)、ハーフバースデー、お誕生日、七五三、成人式、マタニティ、出張撮影、証明写真、その他記念写真などの撮影をいたします。お気軽にお問い合わせください。</p>
</div>

<div class="kids-text">
  <p>ハイハイができるようになった！<br>つかまり立ちができた！<br>あんよが上手になった！</p>
  <p>お子様の成長は早いですね。</p>
  <p>Halfbirthday・1stbirthday・お食い初め・初節句・入園入学・卒園卒業など、見逃したくない一瞬を残してください</p>
</div>
<div class="kids-photo" role="img" aria-label="笑顔でうつ伏せになる赤ちゃんの写真"></div>
<div class="kids-title">元気いっぱいな<br><span class="hl">お子さまの撮影</span><br>はお任せください！</div>

<section class="news">
  <svg class="corner" style="left:60px" width="60" height="40" viewBox="0 0 60 40"><polygon points="0,0 60,0 0,40" fill="#222"/></svg>
  <svg class="corner" style="left:620px" width="60" height="40" viewBox="0 0 60 40"><polygon points="0,0 60,0 0,40" fill="#222"/></svg>
  <div class="news-col" style="left:90px">
    <h3>ブログ</h3>
    <ul><li>2020.12.12 テキストテキストテキストテキスト</li><li>2020.12.12 テキストテキストテキストテキスト</li><li>2020.12.12 テキストテキストテキストテキスト</li></ul>
  </div>
  <div class="news-col" style="left:680px">
    <h3>ニュース</h3>
    <ul><li>2020.12.12 テキストテキストテキストテキスト</li><li>2020.12.12 テキストテキストテキストテキスト</li><li>2020.12.12 テキストテキストテキストテキスト</li></ul>
  </div>
</section>

<h2 class="staff-title">スタッフ紹介</h2>

<article class="staff-card" style="left:70px">
  <div class="bg"></div>
  <div class="photo" role="img" aria-label="女性スタッフのポートレート" style="background:linear-gradient(160deg,#e9dccf,#b89a82)"></div>
  <p class="role">役職テキスト</p><p class="name">山田　花子</p>
  <p class="bio">紹介文が入ります。撮影への思いや得意な撮影、趣味など自己紹介をここに記載します。自己紹介が入ります。</p>
</article>
<article class="staff-card" style="left:428px">
  <div class="bg"></div>
  <div class="photo" role="img" aria-label="スーツ姿の男性スタッフのポートレート" style="background:linear-gradient(160deg,#d7dde0,#6e7a80)"></div>
  <p class="role">役職テキスト</p><p class="name">山田　花子</p>
  <p class="bio">紹介文が入ります。撮影への思いや得意な撮影、趣味など自己紹介をここに記載します。自己紹介が入ります。</p>
</article>
<article class="staff-card" style="left:786px">
  <div class="bg"></div>
  <div class="photo" role="img" aria-label="打ち合わせをするスタッフたちの写真" style="background:linear-gradient(160deg,#eeeeee,#9aa0a4)"></div>
  <p class="role">役職テキスト</p><p class="name">山田　花子</p>
  <p class="bio">紹介文が入ります。撮影への思いや得意な撮影、趣味など自己紹介をここに記載します。自己紹介が入ります。</p>
</article>
</body>
</html>
```